Female Pest Controller needs awesome business cards

I need a logo design for a Pest Control service - something that appeals to 'nature' & safe, with the use of the colour green. I am also female
New Business Name is 'Bug Begone Bay'
appeals to women

Target Market(s)

Domestic Households & Local Businesses

Industry/Entity Type

Pest Control

Contact Information for Business Card

Corinne Waldrake
0428316952
ABN 47 618 259 304
PMT7314958207
Spiders Cockroaches, Ants, Silverfish, Fleas, Rodents

Font styles to use
Decorative

Colors
abd036
aaaaaa
5c5c5c

Requirements
Should not have
• Pics of dead insects, prefer nature inspired designs, frogs, trees etc
• Have attached old log & business name ( now my ex's business) Lilyvale Pest Solutions -

```html
<!DOCTYPE html>
<html lang="en">
<head>
<meta charset="utf-8">
<title>Bug Begone Bay – Business Card</title>
<link rel="stylesheet" href="https://fonts.googleapis.com/css2?family=Open+Sans:wght@400;600;700&display=swap">
<style>
  :root {
    --stage: #0b3d17;
    --card-white: #ffffff;
    --leaf-green: #c2da2f;
    --tree-green: #a9d034;
    --ink: #5c5c5c;
    --ink-soft: #6e6e6e;
    --band: #5c5c5c;
    --band-text: #ffffff;
  }
  * { margin: 0; padding: 0; box-sizing: border-box; }
  html, body {
    width: 1200px;
    height: 1067px;
    overflow: hidden;
    background: var(--stage);
    font-family: "Open Sans", sans-serif;
  }
  .business-card {
    position: absolute;
    left: 160px;
    top: 264px;
    width: 880px;
    height: 538px;
    background: var(--card-white);
    overflow: hidden;
  }
  .tree-artwork {
    position: absolute;
    left: 290px;
    top: 34px;
    width: 290px;
    height: 172px;
    background: radial-gradient(ellipse at 50% 40%, var(--tree-green) 0%, #b6d83a 70%, rgba(182,216,58,0) 100%);
    border-radius: 46% 46% 8px 8px;
  }
  .leaf-field {
    position: absolute;
    left: 0;
    top: 193px;
    width: 880px;
    height: 286px;
    background: var(--leaf-green);
  }
  .brand-name {
    position: absolute;
    top: 214px;
    left: 0;
    width: 100%;
    text-align: center;
    font-size: 56px;
    font-weight: 400;
    color: var(--ink);
    line-height: 1;
  }
  .contact {
    position: absolute;
    top: 328px;
    left: 0;
    width: 100%;
    text-align: center;
    color: var(--ink);
  }
  .contact-name {
    font-size: 32px;
    font-weight: 700;
    line-height: 40px;
  }
  .contact-phone {
    font-size: 36px;
    font-weight: 700;
    line-height: 42px;
    display: inline-flex;
    align-items: center;
    gap: 6px;
  }
  .contact-phone svg { width: 30px; height: 30px; }
  .abn {
    position: absolute;
    top: 430px;
    left: 0;
    width: 100%;
    text-align: center;
    font-size: 25px;
    color: var(--ink-soft);
    text-decoration: underline;
    text-underline-offset: 3px;
  }
  .licence-band {
    position: absolute;
    left: 0;
    top: 479px;
    width: 880px;
    height: 59px;
    background: var(--band);
    color: var(--band-text);
    font-size: 26px;
    line-height: 59px;
    padding-left: 32px;
    white-space: nowrap;
  }
</style>
</head>
<body>
  <div class="business-card">
    <div class="leaf-field" role="img" aria-label="Lime green background with leaf vein texture and grass edge"></div>
    <div class="tree-artwork" role="img" aria-label="Three lime green trees illustration"></div>
    <div class="brand-name">Bug Begone Bay</div>
    <div class="contact">
      <div class="contact-name">Corinne Waldrake</div>
      <div class="contact-phone">
        <svg viewBox="0 0 24 24" aria-hidden="true">
          <circle cx="12" cy="12" r="10.5" fill="none" stroke="#5c5c5c" stroke-width="1.8"/>
          <path d="M8.6 6.8c.4-.3.9-.2 1.1.2l1 1.9c.2.4.1.8-.2 1.1l-.7.6c.6 1.3 1.6 2.4 2.9 3l.6-.7c.3-.3.7-.4 1.1-.2l1.9 1c.4.2.5.7.2 1.1l-.8 1c-.5.5-1.3.7-2 .4-3-1.2-5.3-3.6-6.4-6.6-.2-.7 0-1.4.5-1.9z" fill="#5c5c5c"/>
        </svg>
        0428316952
      </div>
    </div>
    <div class="abn">ABN 47 618 259 304</div>
    <div class="licence-band">PMT Lic: Spiders Cockroaches, Ants, Silverfish, Fleas, Rodents</div>
  </div>
</body>
</html>
```